Erstellung Etikettendesign für Duschgel in Motorölflaschenoptik als Geschenkartikel für Männer
Zielgruppe
Wir sind Versandhändler aus dem Bereich Büro Basteln Schule und Geschenkartikel und verkaufen neben Handelsware aus diesem Bereich auch viele eigene selbst gestaltete Artikel unter unserem Firmennamen morvalo
Aufgabenstellung
Erstellt werden soll ein neues zusätzliches Etikettendesign für unseren Artikel Duschgel für Männer
Das Duschgel wird in Form in einer Motorölflasche geliefert und ist so ein Geschenkartikel für Männer zum Geburtstag, Weihnachten, Vatertag usw.
Die Flaschenfarbe ist immer schwarz
und der Verschluss ist rot
bzgl dem Etikettendesign sind wir für alle kreativen Ideen offen.
Es dürfen allerdings keine anderen Markenrechte verletzt werden
Unter dem Link
https://www.kaufwelt-shop.de/dp/K7R2MXQ9D3
finden sie unsere aktuellen Designs.
Bei solchen Designumsetzungen ist natürlich immer darauf zu achten nicht zu nahe an einem geschützten Produktdesign zu liegen.
Es werden hier mehrere Ideen gesammelt
Es wird bei guten Entwürfen auch mehrere Gewinner geben und mehrere Designs kommen zur Umsetzung.
Nach Auswahl zum Gewinner müssten dann noch die Druckdatei für die Etiketten und ein Produktfoto erstellt werden.
Vorlage für Druckdatei und Beispiel Produktfoto anbei
Aufgabe ist hierbei nicht das Design KL-73 anders umzusetzen sondern andere ganz neue Ideen als Etikett umzusetzen

```html
<!DOCTYPE html>
<html lang="en">
<head>
<meta charset="utf-8">
<title>Men's Shower Gel – Label Concepts</title>
<link rel="stylesheet" href="https://fonts.googleapis.com/css2?family=Anton&display=swap">
<style>
  :root {
    --page-bg: #ffffff;
    --navy: #14202b;
    --label-black: #111111;
    --edge-black: #0c0f12;
    --gold-line: #c9a560;
    --amber: #f0a81e;
    --amber-frame: #e89e1c;
    --red: #e8232a;
    --banner-red: #a52a20;
    --white: #ffffff;
  }
  html, body {
    margin: 0;
    padding: 0;
    width: 1200px;
    height: 857px;
    overflow: hidden;
    background: var(--page-bg);
  }
  .label-sheet {
    display: block;
    width: 1200px;
    height: 857px;
  }
  .label-type {
    font-family: "Anton", "Oswald", sans-serif;
    text-anchor: start;
  }
  .fill-white { fill: var(--white); }
  .fill-red { fill: var(--red); }
  .fill-amber { fill: var(--amber); }
  .classic-body { fill: var(--navy); stroke: var(--edge-black); stroke-width: 10; stroke-linejoin: round; }
  .classic-inner-line { fill: none; stroke: var(--gold-line); stroke-width: 4; stroke-linejoin: round; }
  .classic-banner { fill: var(--banner-red); }
  .workshop-body { fill: var(--label-black); stroke: var(--amber-frame); stroke-width: 15; stroke-linejoin: round; }
  .emblem-placeholder { fill: var(--white); }
</style>
</head>
<body>
<svg class="label-sheet" viewBox="0 0 1200 857" xmlns="http://www.w3.org/2000/svg">

  <!-- Classic label -->
  <g class="label-classic">
    <path class="classic-body" d="M146,720 L146,420 Q150,150 252,66 Q258,62 266,62 L350,62 Q358,62 364,68 L522,234 Q528,240 528,250 L528,720 Q528,748 500,748 L174,748 Q146,748 146,720 Z"/>
    <path class="classic-inner-line" d="M162,714 L162,422 Q166,162 262,80 L348,80 L512,250 L512,714 Q512,732 494,732 L180,732 Q162,732 162,714 Z"/>

    <rect class="fill-white" role="img" aria-label="Moustache illustration" x="226" y="192" width="184" height="60" rx="30"/>

    <text class="label-type fill-white" x="230" y="350" font-size="72" textLength="205" lengthAdjust="spacingAndGlyphs">MEN’S</text>
    <text class="label-type fill-red" x="174" y="450" font-size="76" textLength="323" lengthAdjust="spacingAndGlyphs">SHOWER</text>
    <text class="label-type fill-amber" x="266" y="537" font-size="78" textLength="146" lengthAdjust="spacingAndGlyphs">GEL</text>

    <path class="classic-banner" d="M184,614 L501,614 L488,638 L501,663 L488,688 L501,713 L184,713 L197,688 L184,663 L197,638 Z"/>
    <text class="label-type fill-amber" x="251" y="655" font-size="32" textLength="180" lengthAdjust="spacingAndGlyphs">FOR HARD-</text>
    <text class="label-type fill-amber" x="229" y="698" font-size="32" textLength="230" lengthAdjust="spacingAndGlyphs">WORKING MEN</text>
  </g>

  <!-- Workshop label -->
  <g class="label-workshop">
    <path class="workshop-body" d="M672,113 L918,113 L1087,285 L1087,735 Q1087,774 1048,774 L670,774 Q631,774 631,735 L631,152 Q631,113 672,113 Z"/>

    <text class="label-type fill-white" x="706" y="311" font-size="92" textLength="268" lengthAdjust="spacingAndGlyphs">MEN’S</text>
    <text class="label-type fill-red" x="688" y="402" font-size="92" textLength="309" lengthAdjust="spacingAndGlyphs">SHOWER</text>

    <circle class="emblem-placeholder" role="img" aria-label="Gear emblem with shower head" cx="773" cy="515" r="84"/>

    <text class="label-type fill-amber" x="856" y="543" font-size="100" textLength="196" lengthAdjust="spacingAndGlyphs">GEL</text>

    <text class="label-type fill-amber" x="685" y="664" font-size="56" textLength="289" lengthAdjust="spacingAndGlyphs">FOR HARD-</text>
    <text class="label-type fill-amber" x="685" y="727" font-size="56" textLength="349" lengthAdjust="spacingAndGlyphs">WORKING MEN</text>
  </g>

</svg>
</body>
</html>
```